PowerPoint Design for TALLY Polls

TALLY Polls stands for 'Tracking Attitudes Linked Lately Yearly Polls'. It is a collaborative research effort to format and combine multiple sources of public opinion data from around the world into merged datasets. We need a Microsoft PowerPoint design for our conference/workshop presentations and instructional videos used as part of our research efforts and crowdsourced development. The design should match the website design and logo, which are attached to this contest (these are the files from previous successful design contests).

Slides will contain a lot of data visualizations, tables with statistical output (lots of numbers), and figures. Bullet points will be used frequently on slides and larg blocks of text should be avided. Margins should be narrow to maximize space used and the size of fonts must be large enough (24-32+) to be visible at the back of classrooms and conference rooms.
Updates

I was away at a conference and am now busy with teaching preparation, so I need a few extra days to give adequate feedback.

Target Market(s)

academia, government, non-profits, postgraduates, researchers

Font styles to use
Sans Serif

Colors

Designer to choose colors to be used in the design.

Requirements
Must have
• designs for common slide layouts
Nice to have
• thematic link with website design and logo

```html
<!DOCTYPE html>
<html lang="en">
<head>
<meta charset="utf-8">
<title>TALLY Polls – Presentation Template Sheet</title>
<link href="https://fonts.googleapis.com/css2?family=Open+Sans:wght@400;600;700&display=swap" rel="stylesheet">
<style>
:root{
  --page:#cdced0;
  --paper:#ffffff;
  --blue:#1a75c8;
  --blue-dark:#0e5fa8;
  --blue-mid:#2f8fdc;
  --blue-pale:#dceefa;
  --blue-soft:#bcdcf3;
  --ink:#2b2b2b;
  --muted:#6b6f73;
  --rule:#9cc5e8;
}
*{box-sizing:border-box;margin:0;padding:0}
html,body{width:1200px;height:1200px;overflow:hidden;background:var(--page);font-family:"Open Sans",Arial,sans-serif;color:var(--ink)}
.sheet{position:relative;width:1200px;height:1200px}
.slide{position:absolute;width:360px;height:270px;background:var(--paper);box-shadow:0 2px 5px rgba(0,0,0,.28);overflow:hidden}
.c1{left:33px}.c2{left:420px}.c3{left:807px}
.r1{top:26px}.r2{top:315px}.r3{top:600px}.r4{top:894px}
.abs{position:absolute}
/* header */
.headline{position:absolute;left:16px;right:16px;top:10px;text-align:center;font-size:11px;letter-spacing:.2px;color:#222;padding:3px 0 2px;border-top:1px dashed var(--rule);border-bottom:1px dashed var(--rule);line-height:12px}
.headline span{color:var(--blue)}
/* footer */
.foot{position:absolute;left:0;right:0;bottom:6px;height:7px}
.foot .url{position:absolute;left:0;top:0;width:250px;height:5px;background:var(--blue);color:#fff;font-size:3.6px;line-height:5px;padding-left:20px}
.foot .url::after{content:"";position:absolute;right:0;top:0}
.foot .brand{position:absolute;left:262px;top:-5px;font-size:6px;color:var(--blue);font-weight:600;display:flex;align-items:center;gap:2px}
.dot{display:inline-block;width:6px;height:6px;border-radius:50%;background:var(--blue-mid)}
.foot .num{position:absolute;right:8px;top:0;width:28px;height:5px;background:var(--blue);color:#fff;font-size:4.5px;line-height:5px;text-align:center;clip-path:polygon(12% 0,100% 0,100% 100%,0 100%)}
.foot::before{content:"";position:absolute;left:250px;right:36px;top:3px;height:1px;background:var(--rule)}
/* type */
.t-tiny{font-size:3.8px;line-height:5.2px;color:#333}
.t-small{font-size:4.4px;line-height:6px;color:#333}
.t-head{font-size:6.4px;font-weight:700;color:#111;line-height:8px}
.t-blue{color:var(--blue);font-weight:600}
.photo{position:absolute;background:linear-gradient(135deg,#b9c9d8,#6f8aa3 55%,#3d546b)}
.photo.light{background:linear-gradient(160deg,#ffffff,#e9eef2 60%,#c9d3dc)}
.photo.circle{border-radius:50%;border:2px solid var(--blue-mid)}
/* cover */
.cover-brand{position:absolute;right:20px;top:24px;display:flex;align-items:center;gap:5px;color:var(--blue);font-size:16px;font-weight:600}
.cover-brand .dot{width:14px;height:14px}
.deco{position:absolute;border-radius:50%;background:radial-gradient(circle,#cfe6f7 0%,#e6f2fb 70%,rgba(255,255,255,0) 71%)}
.cover-title{position:absolute;left:102px;top:183px;font-size:14.5px;line-height:17px;font-weight:700}
.cover-title .a{color:var(--blue)}.cover-title .b{color:#555}
.cover-sub{position:absolute;left:102px;top:228px;font-size:6.4px;color:var(--blue);letter-spacing:.2px}
/* toc */
.toc-title{position:absolute;left:16px;right:16px;top:10px;text-align:center;font-size:10px;border-bottom:1px solid var(--blue);padding-bottom:3px;border-top:1px dashed var(--rule);padding-top:3px}
.toc{position:absolute;left:16px;top:44px;display:grid;grid-template-columns:repeat(3,110px);row-gap:20px;column-gap:8px}
.toc-item{display:flex;gap:5px;align-items:flex-start}
.toc-num{flex:none;width:13px;height:13px;border-radius:50%;background:var(--blue);color:#fff;font-size:5px;line-height:13px;text-align:center;margin-top:4px}
.toc-item b{display:block;font-size:7px;font-weight:400;color:var(--blue);line-height:9px;border-left:1px solid var(--rule);padding-left:3px}
.toc-item i{display:block;font-style:normal;font-size:3.6px;color:#888;line-height:4.8px;padding-left:4px;border-left:1px solid var(--rule)}
/* team */
.card{position:absolute;top:115px;width:90px;height:127px;background:var(--blue-pale);padding:3px 6px}
.card .t-blue{font-size:5.4px;line-height:6.5px;display:block;margin-bottom:3px}
/* table */
.data{position:absolute;left:22px;top:83px;width:324px;border-collapse:collapse;font-size:3.8px}
.data th{background:var(--blue-mid);color:#fff;font-weight:600;height:12px;text-align:left;padding-left:5px;border-right:1px solid #fff}
.data td{height:13.4px;padding-left:5px;border-bottom:1px solid #e2edf6;border-right:1px solid #fff;color:#333}
.data td:first-child{text-align:center;padding:0}
.data td.n{text-align:center;padding:0}
.data tr:nth-child(even) td{background:#eef6fc}
.data td:first-child,.data td:nth-child(2){background:#e2f0fa}
/* bullets */
.bul{list-style:none}
.bul li{position:relative;padding-left:7px;margin-bottom:5px}
.bul li::before{content:"";position:absolute;left:0;top:1px;width:3px;height:3px;border:.6px solid var(--blue);border-radius:.5px}
.icon-c{position:absolute;width:14px;height:14px;border-radius:50%;border:1.5px solid #888;background:#fff}
.icon-c::after{content:"";position:absolute;inset:3px;border-radius:50%;background:#888}
/* thank you */
.thanks{position:absolute;left:26px;top:177px;font-size:15px;font-weight:700;color:var(--blue-mid)}
.ty-brand{position:absolute;left:26px;top:228px;display:flex;align-items:center;gap:3px;font-size:8px;font-weight:600;color:var(--blue)}
.ty-contact{position:absolute;left:128px;top:222px;display:flex;gap:8px;font-size:3.6px;line-height:5px;color:#333;border-left:1px solid var(--blue);padding-left:4px}
.ty-contact .pin{display:flex;gap:2px;align-items:flex-start}
.ty-contact .ic{width:4px;height:4px;border-radius:50%;background:var(--blue);flex:none;margin-top:.5px}
.ty-contact .addr{color:var(--blue);border-left:1px solid var(--blue);padding-left:4px}
</style>
</head>
<body>
<div class="sheet">

<!-- 1 cover -->
<section class="slide c1 r1" aria-label="Cover slide">
  <div class="deco" style="left:-70px;top:40px;width:190px;height:190px"></div>
  <div class="cover-brand"><span class="dot"></span>TALLY Polls</div>
  <h1 class="cover-title"><span class="a">LOREM IPSUM IS SIMPLY</span><br><span class="b">DUMMY HAS BEEN</span></h1>
  <p class="cover-sub">LOREM IPSUM IS SIMPLY DUMMY HAS BEEN</p>
</section>

<!-- 2 table of contents -->
<section class="slide c2 r1" aria-label="Table of contents slide">
  <div class="toc-title">TABLE OF CONTENTS</div>
  <div class="toc">
    <div class="toc-item"><span class="toc-num">1</span><div><b>About Us</b><i>Lorem Ipsum is simply dummy<br>text of the printing and</i></div></div>
    <div class="toc-item"><span class="toc-num">2</span><div><b>Who We Are</b><i>Lorem Ipsum is simply dummy<br>text of the printing and</i></div></div>
    <div class="toc-item"><span class="toc-num">3</span><div><b>What We Do</b><i>Lorem Ipsum is simply dummy<br>text of the printing and</i></div></div>
    <div class="toc-item"><span class="toc-num">4</span><div><b>About Us</b><i>Lorem Ipsum is simply dummy<br>text of the printing and</i></div></div>
    <div class="toc-item"><span class="toc-num">5</span><div><b>About Us</b><i>Lorem Ipsum is simply dummy<br>text of the printing and</i></div></div>
    <div class="toc-item"><span class="toc-num">6</span><div><b>About Us</b><i>Lorem Ipsum is simply dummy<br>text of the printing and</i></div></div>
    <div class="toc-item"><span class="toc-num">7</span><div><b>About Us</b><i>Lorem Ipsum is simply dummy<br>text of the printing and</i></div></div>
    <div class="toc-item"><span class="toc-num">8</span><div><b>About Us</b><i>Lorem Ipsum is simply dummy<br>text of the printing and</i></div></div>
    <div class="toc-item"><span class="toc-num">9</span><div><b>About Us</b><i>Lorem Ipsum is simply dummy<br>text of the printing and</i></div></div>
    <div class="toc-item"><span class="toc-num">7</span><div><b>About Us</b><i>Lorem Ipsum is simply dummy<br>text of the printing and</i></div></div>
    <div class="toc-item"><span class="toc-num">8</span><div><b>About Us</b><i>Lorem Ipsum is simply dummy<br>text of the printing and</i></div></div>
    <div class="toc-item"><span class="toc-num">9</span><div><b>About Us</b><i>Lorem Ipsum is simply dummy<br>text of the printing and</i></div></div>
  </div>
  <div class="foot"><div class="url">www.tallypolls.org</div><div class="brand"><span class="dot"></span>TALLY Polls</div><div class="num">01</div></div>
</section>

<!-- 3 team -->
<section class="slide c3 r1" aria-label="Three column profile slide">
  <div class="headline">HEADLINE <span>HERE</span></div>
  <div class="photo circle" style="left:40px;top:40px;width:62px;height:62px" role="img" aria-label="Portrait photo of a businessman at his desk"></div>
  <div class="photo circle light" style="left:150px;top:40px;width:62px;height:62px" role="img" aria-label="Portrait photo of an office worker on the phone"></div>
  <div class="photo circle light" style="left:265px;top:40px;width:62px;height:62px" role="img" aria-label="Photo of a person behind a stack of paperwork"></div>
  <div class="card t-tiny" style="left:27px"><span class="t-blue">Lorem ipsum dolor sit<br>amet, consectetur adip-</span>Lorem Ipsum is simply dummy text of the printing and typesetting industry. Lorem Ipsum has been the industry's standard dummy text ever since the 1500s, when an unknown printer took a galley of type and scrambled it to make a type specimen book. It has survived not only five centuries, but also the leap into electronic typesetting, remaining essentially unchanged. It was popularised in the 1960s with the</div>
  <div class="card t-tiny" style="left:141px"><span class="t-blue">Lorem ipsum dolor sit<br>amet, consectetur adip-</span>Lorem Ipsum is simply dummy text of the printing and typesetting industry. Lorem Ipsum has been the industry's standard dummy text ever since the 1500s, when an unknown printer took a galley of type and scrambled it to make a type specimen book. It has survived not only five centuries, but also the leap into electronic typesetting, remaining essentially unchanged. It was</div>
  <div class="card t-tiny" style="left:255px"><span class="t-blue">Lorem ipsum dolor sit<br>amet, consectetur adip-</span>Lorem Ipsum is simply dummy text of the printing and typesetting industry. Lorem Ipsum has been the industry's standard dummy text ever since the 1500s, when an unknown printer took a galley of type and scrambled it to make a type specimen book. It has survived not only five centuries, but also the leap into electronic typesetting, remaining essentially unchanged. It was</div>
  <div class="foot"><div class="url">www.tallypolls.org</div><div class="brand"><span class="dot"></span>TALLY Polls</div><div class="num">01</div></div>
</section>

<!-- 4 table -->
<section class="slide c1 r2" aria-label="Data table slide">
  <div class="headline">HEADLINE <span>HERE</span></div>
  <p class="t-head abs" style="left:22px;top:40px;width:330px;white-space:nowrap;overflow:hidden">Lorem ipsum dolor sit amet, consectetur adipisicing elit, sed do eiusmod tempor incid-</p>
  <p class="t-tiny abs" style="left:22px;top:50px;width:328px">Lorem Ipsum is simply dummy text of the printing and typesetting industry. Lorem Ipsum has been the industry's standard dummy text ever since the 1500s, when an unknown printer took a galley of type and scrambled it to make a type specimen book. It has survived not only five centuries, but also the leap into electronic typesetting, remaining essentially unchanged. It was popularised in</p>
  <table class="data">
    <thead><tr><th style="width:20px"></th><th style="width:105px">Lorem ipsum is simply dummy text of</th><th style="width:85px">Lorem Ipsum is simply</th><th style="width:60px">Lorem Ipsum</th><th>Lorem Ipsum</th></tr></thead>
    <tbody>
      <tr><td>1</td><td>Lorem Ipsum is simply dummy text of the</td><td>Lorem Ipsum is simply dummy</td><td class="n">109</td><td class="n">2190</td></tr>
      <tr><td>2</td><td>Lorem Ipsum is simply dummy</td><td>Lorem Ipsum is simply dummy</td><td class="n">109</td><td class="n">2190</td></tr>
      <tr><td>3</td><td>Lorem Ipsum is simply dummy text of the</td><td>Lorem Ipsum is simply dummy</td><td class="n">109</td><td class="n">2190</td></tr>
      <tr><td>4</td><td>Lorem Ipsum is simply dummy text of the</td><td>Lorem Ipsum is simply dummy</td><td class="n">109</td><td class="n">2190</td></tr>
      <tr><td>5</td><td>Lorem Ipsum is</td><td>Lorem Ipsum is simply dummy</td><td class="n">109</td><td class="n">2190</td></tr>
      <tr><td>0</td><td>Lorem Ipsum is simply</td><td>Lorem Ipsum is simply dummy</td><td class="n">109</td><td class="n">2190</td></tr>
      <tr><td>0</td><td>Lorem Ipsum is simply dummy text of</td><td>Lorem Ipsum is simply dummy</td><td class="n">109</td><td class="n">2190</td></tr>
      <tr><td>0</td><td>Lorem Ipsum is simply dummy text of the</td><td>Lorem Ipsum is simply dummy</td><td class="n">109</td><td class="n">2190</td></tr>
      <tr><td>0</td><td>Lorem Ipsum is simply dummy text of the</td><td>Lorem Ipsum is simply dummy</td><td class="n">109</td><td class="n">2190</td></tr>
      <tr><td>0</td><td>Lorem Ipsum is</td><td>Lorem Ipsum is simply dummy</td><td class="n">109</td><td class="n">2190</td></tr>
      <tr><td>0</td><td>Lorem Ipsum is simply</td><td>Lorem Ipsum is simply dummy</td><td class="n">109</td><td class="n">2190</td></tr>
    </tbody>
  </table>
  <div class="foot"><div class="url">www.tallypolls.org</div><div class="brand"><span class="dot"></span>TALLY Polls</div><div class="num">01</div></div>
</section>

<!-- 5 bar chart -->
<section class="slide c2 r2" aria-label="Bar chart slide">
  <div class="headline">HEADLINE <span>HERE</span></div>
  <svg class="abs" style="left:20px;top:108px" width="200" height="130" viewBox="0 0 200 130" font-family="Open Sans, sans-serif" font-size="4" fill="#333">
    <line x1="4" y1="115" x2="196" y2="115" stroke="#bbb" stroke-width=".5"/>
    <g fill="#3d8fd6">
      <rect x="8" y="65" width="14" height="50"/><rect x="24" y="54" width="14" height="61"/><rect x="40" y="75" width="14" height="40"/>
      <rect x="56" y="93" width="14" height="22"/><rect x="72" y="110" width="14" height="5"/><rect x="88" y="94" width="14" height="21"/>
      <rect x="104" y="96" width="14" height="19"/><rect x="120" y="106" width="14" height="9"/><rect x="136" y="92" width="14" height="23"/>
      <rect x="152" y="69" width="14" height="46"/><rect x="168" y="61" width="14" height="54"/><rect x="184" y="35" width="14" height="80"/>
    </g>
    <g text-anchor="middle">
      <text x="15" y="62">120</text><text x="31" y="51">146</text><text x="47" y="72">96</text><text x="63" y="90">53</text>
      <text x="79" y="107">11</text><text x="95" y="91">50.5</text><text x="111" y="93">46</text><text x="127" y="103">20.9</text>
      <text x="143" y="89">55</text><text x="159" y="66">109</text><text x="175" y="58">129</text><text x="191" y="32">189</text>
      <text x="15" y="122">Jan</text><text x="31" y="122">Febr</text><text x="47" y="122">March</text><text x="63" y="122">April</text>
      <text x="79" y="122">May</text><text x="95" y="122">Jun</text><text x="111" y="122">July</text><text x="127" y="122">Aug</text>
      <text x="143" y="122">Sep</text><text x="159" y="122">Oct</text><text x="175" y="122">Nov</text><text x="191" y="122">Dec</text>
    </g>
  </svg>
  <p class="t-blue abs" style="left:240px;top:55px;font-size:6.4px;line-height:7px">Lorem ipsum dolor sit amet,<br>consectetur adipisicing elit,</p>
  <ul class="bul t-tiny abs" style="left:240px;top:75px;width:106px">
    <li>Lorem Ipsum is simply dummy text of the printing and typesetting industry. Lorem Ipsum has been the industry's standard dummy tex</li>
    <li>Ever since the 1500s, when an unknown printer took a galley of type and scrambled it to make a type specimen book.</li>
    <li>It has survived not only five centuries, but also the leap into electronic typesetting, remaining essentially unchanged. It was popularised in the 1960s with the release of</li>
    <li>It is a long established fact that a reader will be distracted by the readable content of a page when looking at its layout. The point of using</li>
    <li>Lorem Ipsum is that it has a more-or-less normal distribution of letters, as opposed to using 'Content here, content here', making it look like readable English. Many desktop publishing packages and web page editors</li>
  </ul>
  <div class="foot"><div class="url">www.tallypolls.org</div><div class="brand"><span class="dot"></span>TALLY Polls</div><div class="num">01</div></div>
</section>

<!-- 6 image with bullets -->
<section class="slide c3 r2" aria-label="Image and bullet points slide">
  <div class="headline">HEADLINE <span>HERE</span></div>
  <p class="t-tiny abs" style="left:22px;top:36px;width:325px">Lorem Ipsum is simply dummy text of the printing and typesetting industry. Lorem Ipsum has been the industry's standard dummy text ever since the 1500s, when an unknown printer took a galley of type and scrambled it to make a type specimen book. It has survived not only five centuries, but also the leap into electronic typesetting, remaining essentially unchanged. It was popularised in the 1960s with the release of L</p>
  <div class="photo" style="left:30px;top:112px;width:190px;height:120px;background:linear-gradient(135deg,#e4ecf3,#9fb3c6 55%,#5d7790)" role="img" aria-label="Photo of a relaxed businessman leaning back at his office desk"></div>
  <ul class="bul t-tiny abs" style="left:233px;top:88px;width:115px;font-size:3.5px;line-height:4.6px">
    <li>Lorem Ipsum is simply dummy text of the printing and typesetting industry. Lorem Ipsum has been the industry's standard dummy tex</li>
    <li>Ever since the 1500s, when an unknown printer took a galley of type and scrambled it to make a type specimen book.</li>
    <li>It has survived not only five centuries, but also the leap into electronic typesetting, remaining essentially unchanged. It was popularised in the 1960s with the release of</li>
    <li>It is a long established fact that a reader will be distracted by the readable content of a page when looking at its layout. The point of using</li>
    <li>Lorem Ipsum is that it has a more-or-less normal distribution of letters, as opposed to using 'Content here, content here', making it look like readable English. Many desktop publishing packages and web page editors now use Lorem Ipsum as their default model text, and a search for 'lorem ipsum' will</li>
  </ul>
  <div class="foot"><div class="url">www.tallypolls.org</div><div class="brand"><span class="dot"></span>TALLY Polls</div><div class="num">01</div></div>
</section>

<!-- 7 two images -->
<section class="slide c1 r3" aria-label="Two image columns slide">
  <div class="headline">HEADLINE <span>HERE</span></div>
  <div class="photo" style="left:21px;top:40px;width:146px;height:95px;background:linear-gradient(135deg,#8fa9c0,#4d6a86 55%,#263a50)" role="img" aria-label="Photo of a businessman sketching cloud computing diagrams"></div>
  <div class="photo light" style="left:198px;top:40px;width:146px;height:95px" role="img" aria-label="Photo of a person with a stack of files beside a laptop"></div>
  <p class="t-blue abs" style="left:21px;top:150px;font-size:6.4px">Lorem Ipsum is simply dummy text</p>
  <p class="t-blue abs" style="left:202px;top:150px;font-size:6.4px">Lorem Ipsum is simply dummy text</p>
  <p class="t-tiny abs" style="left:21px;top:163px;width:145px">Lorem Ipsum is simply dummy text of the printing and typesetting industry. Lorem Ipsum has been the industry's standard dummy text ever since the 1500s, when an unknown printer took a galley of type and scrambled it to make a type specimen book. It has survived not only five centuries.<br><br>But also the leap into electronic typesetting, remaining essentially unchanged. It was popularised in the 1960s with the release of sheets containing Lorem Ipsum passages, and more recently with desktop publishing software including versions of Lorem Ipsum. It is a long established fact that a reader will be distracted by the readable</p>
  <p class="t-tiny abs" style="left:202px;top:163px;width:145px">content of a page when looking at its l<br>The point of using Lorem Ipsum is that it has a more-or-less normal distribution of letters, as opposed to using 'Content here, content here', making it look like readable English. Many desktop publishing packages and web page editors now use Lorem Ipsum as their default model text, and a search for 'lorem ipsum' will uncover many web sites still in their infancy. Contrary to popular belief, Lorem Ipsum is not simply random text. It has roots in a piece of classical Latin literature from 45<br><br>BC, making it over 2000 years old. A Latin scholar later looked up one of the more obscure words in a passage and traced its source</p>
  <div class="foot"><div class="url">www.tallypolls.org</div><div class="brand"><span class="dot"></span>TALLY Polls</div><div class="num">01</div></div>
</section>

<!-- 8 donuts -->
<section class="slide c2 r3" aria-label="Percentage charts slide">
  <div class="headline">HEADLINE <span>HERE</span></div>
  <p class="t-head abs" style="left:21px;top:38px;width:330px;white-space:nowrap;overflow:hidden">Lorem ipsum dolor sit amet, consectetur adipisicing elit, sed do eiusmod tempor incid-</p>
  <p class="t-tiny abs" style="left:21px;top:48px;width:325px">Lorem Ipsum is simply dummy text of the printing and typesetting industry. Lorem Ipsum has been the industry's standard dummy text ever since the 1500s, when an unknown printer took a galley of type and scrambled it to make a type specimen book. It has survived not only five centuries, but also the leap into electronic typesetting, remaining essentially unchanged. It was popularised in</p>
  <svg class="abs" style="left:20px;top:90px" width="330" height="80" viewBox="0 0 330 80" font-family="Open Sans, sans-serif" font-size="5.5" fill="#333">
    <g fill="none" stroke-width="6">
      <circle cx="54" cy="38" r="25" stroke="#2f8fdc"/><circle cx="54" cy="38" r="25" stroke="#8cc4ee" stroke-dasharray="20 157" transform="rotate(-100 54 38)"/>
      <circle cx="170" cy="38" r="25" stroke="#2f8fdc"/><circle cx="170" cy="38" r="25" stroke="#8cc4ee" stroke-dasharray="20 157" transform="rotate(-100 170 38)"/>
      <circle cx="286" cy="38" r="25" stroke="#2f8fdc"/><circle cx="286" cy="38" r="25" stroke="#8cc4ee" stroke-dasharray="20 157" transform="rotate(-100 286 38)"/>
    </g>
    <text x="0" y="17">00%</text><text x="88" y="63">00%</text>
    <text x="117" y="17">00%</text><text x="206" y="63">00%</text>
    <text x="230" y="17">00%</text>
  </svg>
  <p class="t-tiny abs" style="left:21px;top:175px;width:88px">Lorem Ipsum is simply dummy text of the printing and typesetting industry. Lorem Ipsum has been the industry's standard dummy text ever since the 1500s, when an unknown printer took a galley of type and scrambled it to make a type specimen book. It has</p>
  <p class="t-tiny abs" style="left:138px;top:175px;width:88px">Lorem Ipsum is simply dummy text of the printing and typesetting industry. Lorem Ipsum has been the industry's standard dummy text ever since the 1500s, when an unknown printer took a galley of type and scrambled it to make a type specimen book. It has</p>
  <p class="t-tiny abs" style="left:254px;top:175px;width:88px">Lorem Ipsum is simply dummy text of the printing and typesetting industry. Lorem Ipsum has been the industry's standard dummy text ever since the 1500s, when an unknown printer took a galley of type and scrambled it to make a type specimen book. It has</p>
  <div class="foot"><div class="url">www.tallypolls.org</div><div class="brand"><span class="dot"></span>TALLY Polls</div><div class="num">01</div></div>
</section>

<!-- 9 images with icon points -->
<section class="slide c3 r3" aria-label="Images with icon points slide">
  <div class="headline">HEADLINE <span>HERE</span></div>
  <div class="photo" style="left:21px;top:42px;width:146px;height:100px;background:linear-gradient(135deg,#8fa9c0,#4d6a86 55%,#263a50)" role="img" aria-label="Photo of a businessman drawing cloud network diagrams"></div>
  <div class="photo" style="left:21px;top:147px;width:146px;height:88px;background:linear-gradient(135deg,#e4ecf3,#9fb3c6 55%,#5d7790)" role="img" aria-label="Photo of a businessman relaxing at his office desk"></div>
  <span class="icon-c" style="left:204px;top:42px"></span>
  <p class="abs" style="left:230px;top:44px;font-size:6.4px;color:#777">Lorem ipsum dolor sit amet,</p>
  <p class="t-tiny abs" style="left:230px;top:58px;width:115px">Lorem Ipsum is simply dummy text of the printing and typesetting industry. Lorem Ipsum has been the industry's standard dummy text ever since the 1500s, when an unknown printer took a galley of type and scrambled it to make a type specimen book. It has survived not only five centuries, but also the leap into electronic typesetting, remaining essentially unchanged. It was popularised in</p>
  <span class="icon-c" style="left:204px;top:150px"></span>
  <p class="abs" style="left:230px;top:152px;font-size:6.4px;color:#777">Lorem ipsum dolor sit amet,</p>
  <p class="t-tiny abs" style="left:230px;top:166px;width:115px">Lorem Ipsum is simply dummy text of the printing and typesetting industry. Lorem Ipsum has been the industry's standard dummy text ever since the 1500s, when an unknown printer took a galley of type and scrambled it to make a type specimen book. It has survived not only five centuries, but also</p>
  <div class="foot"><div class="url">www.tallypolls.org</div><div class="brand"><span class="dot"></span>TALLY Polls</div><div class="num">01</div></div>
</section>

<!-- 10 text slide -->
<section class="slide c1 r4" aria-label="Text content slide">
  <div class="headline">HEADLINE <span>HERE</span></div>
  <p class="abs" style="left:20px;top:37px;font-size:8px;font-weight:600">Solution</p>
  <p class="abs" style="left:20px;top:52px;font-size:4px;color:var(--blue)">AI automated accounting</p>
  <p class="t-tiny abs" style="left:20px;top:58px;width:330px;line-height:5.4px">LedgerLoop builds automation in stages on top of its current system to reach full automation thanks to the LedgerLoop AI. LedgerLoop AI automates every manual task performed by the user. It starts by connecting to all sources of accounting data such as bank accounts, credit card, webshop or document management systems (CloudCrate or VaultNet). Based on these data, LedgerLoop AI creates bookings and generates financial reports. Finally, LedgerLoop AI features chat-like interface that allows users to communicate seamlessly with it, viewing it as a trusted advisor over time for all their accounting queries.</p>
  <p class="abs" style="left:20px;top:108px;font-size:4px;color:var(--blue)">Blockchain software license or Token-as-a-License (TaaL)</p>
  <p class="t-tiny abs" style="left:20px;top:114px;width:330px;line-height:5.4px">It is possible to create tokens on blockchain that represent software licenses, also known as Token-as-a-Licence (TaaL). LedgerLoop creates TaaL by using the Bramblechain official wallet which interacts with the Bramblechain. Upon purchase of TaaL, the token holder is free to transfer or sell TaaL using secondary market that is built directly over the blockchain, in our case, the Bramblechain marketplace. LedgerLoop checks the validity of a token against the blockchain ensuring that token holders have access to the software. TaaL make distribution and securisation of software licenses easier for software developers. It also makes the management and resale of software license easier for software owners. All in all, TaaL has a higher value as a normal software license.</p>
  <p class="abs" style="left:20px;top:184px;font-size:8px;font-weight:600">Pre-ICO Token sale</p>
  <p class="t-tiny abs" style="left:20px;top:196px;width:330px;line-height:5.4px">To realize this innovative vision, LedgerLoop is launching a pre-ICO in form of a token sale on Bramblechain. 20,000,000 tokens are available to purchase for the price of CHF 0.10 each during a 30-day period to be announced. Tokens represent LedgerLoop lifelong software licenses and by purchasing enough tokens, holders gain access to LedgerLoop software. 15,000 tokens give access to LedgerLoop invoicing or accounting. 20,000 tokens give access to both LedgerLoop accounting and invoicing. Future customers will still have the opportunity to buy</p>
  <div class="foot"><div class="url">www.tallypolls.org</div><div class="brand"><span class="dot"></span>TALLY Polls</div><div class="num">01</div></div>
</section>

<!-- 11 thank you -->
<section class="slide c2 r4" aria-label="Closing slide">
  <div class="deco" style="left:230px;top:20px;width:190px;height:190px"></div>
  <p class="thanks">THANK YOU</p>
  <div class="ty-brand"><span class="dot"></span>TALLY Polls</div>
  <div class="ty-contact">
    <div><div class="pin"><span class="ic"></span>000-555-0147 Ext 12</div><div class="pin"><span class="ic"></span>hello@tallypolls.org</div><div class="pin"><span class="ic"></span>www.tallypolls.org</div></div>
    <div class="addr">12 Meadow Row<br>Fernvale Harbour FV 4820</div>
  </div>
</section>

</div>
</body>
</html>
```